We Walk Under Sky needs a canvas shopping bag design

Dear Designers,
I have a registered Trade Mark Logo that I want incorporated on a canvas shopping bag “We Walk Under Sky” One side will have the logo and added design to compliment it and the other side is going to be quotes from everyday people ( you and I :º) I will provide the first quote but will need the final design to allow me to change that quote i.e. psd. Please add design to compliment the quotes.
The quote should say “There is only one race the human race and we all belong to it.” Morris WWII Combat vet ex POW….1964.

I look forward to seeing your designs and I hope the quote itself inspires you.

Thanks,
Dot

Target Market(s)

Consumers, stores....

Industry/Entity Type

Shopping

Font styles to use
Script

Requirements
Must have
• Room for content, also a handwritten font but not fancy.
Nice to have
• Something universal that resonates with all human beings.
Should not have
• Nothing religious or political that would alienate anyone one.

```html
<!DOCTYPE html>
<html lang="en">
<head>
<meta charset="utf-8">
<title>We Walk Under Sky – Quote Bag Side</title>
<link rel="stylesheet" href="https://fonts.googleapis.com/css2?family=Pinyon+Script&family=Arimo&display=swap">
<style>
  :root {
    --paper: #ffffff;
    --frame-green: #718a68;
    --panel-grey: #e1e5e5;
    --ink: #111111;
    --leaf-light: #a6e05a;
    --leaf-deep: #5cb533;
  }
  html, body {
    margin: 0;
    padding: 0;
    width: 1200px;
    height: 932px;
    overflow: hidden;
    background: var(--paper);
  }
  .bag-side {
    display: block;
    width: 1200px;
    height: 932px;
  }
  .frame-band { fill: var(--frame-green); }
  .frame-gap { fill: var(--paper); }
  .frame-panel { fill: var(--panel-grey); }
  .quote-line {
    font-family: "Pinyon Script", cursive;
    font-size: 74px;
    fill: var(--ink);
    text-anchor: middle;
  }
  .attribution {
    font-family: "Arimo", Arial, sans-serif;
    font-size: 33px;
    fill: var(--ink);
    text-anchor: middle;
  }
</style>
</head>
<body>
<svg class="bag-side" viewBox="0 0 1432 1112" xmlns="http://www.w3.org/2000/svg">
  <defs>
    <radialGradient id="ivy-glow" cx="0.5" cy="0.5" r="0.5">
      <stop offset="0" stop-color="var(--leaf-deep)" stop-opacity="0.55"/>
      <stop offset="0.55" stop-color="var(--leaf-light)" stop-opacity="0.4"/>
      <stop offset="1" stop-color="var(--leaf-light)" stop-opacity="0"/>
    </radialGradient>
  </defs>

  <!-- climbing ivy areas, set behind the frame -->
  <g class="ivy-area">
    <ellipse role="img" aria-label="Climbing ivy vine with green leaves and curling tendrils, top left corner"
             fill="url(#ivy-glow)" cx="300" cy="290" rx="290" ry="270" transform="rotate(-20 300 290)"/>
    <ellipse role="img" aria-label="Climbing ivy vine with green leaves and curling tendrils, bottom right corner"
             fill="url(#ivy-glow)" cx="1090" cy="840" rx="290" ry="250" transform="rotate(-25 1090 840)"/>
  </g>

  <!-- ornate frame, built from nested layers -->
  <g class="frame-band">
    <rect x="80" y="420" width="1205" height="315" rx="157"/>
    <rect x="190" y="262" width="980" height="540"/>
    <rect x="278" y="225" width="807" height="634"/>
    <ellipse cx="710" cy="560" rx="400" ry="388"/>
  </g>
  <g class="frame-gap">
    <rect x="102" y="442" width="1161" height="271" rx="135"/>
    <rect x="212" y="284" width="936" height="496"/>
    <rect x="300" y="247" width="763" height="590"/>
    <ellipse cx="710" cy="560" rx="378" ry="366"/>
  </g>
  <g class="frame-band">
    <rect x="116" y="456" width="1133" height="243" rx="121"/>
    <rect x="226" y="298" width="908" height="468"/>
    <rect x="314" y="261" width="735" height="562"/>
    <ellipse cx="710" cy="560" rx="364" ry="352"/>
  </g>
  <g class="frame-gap">
    <rect x="128" y="468" width="1109" height="219" rx="109"/>
    <rect x="238" y="310" width="884" height="444"/>
    <rect x="326" y="273" width="711" height="538"/>
    <ellipse cx="710" cy="560" rx="352" ry="340"/>
  </g>
  <g class="frame-panel">
    <rect x="136" y="476" width="1093" height="203" rx="101"/>
    <rect x="246" y="318" width="868" height="428"/>
    <rect x="334" y="281" width="695" height="522"/>
    <ellipse cx="710" cy="560" rx="344" ry="332"/>
  </g>

  <!-- quote -->
  <text class="quote-line" x="690" y="405">There is only</text>
  <text class="quote-line" x="678" y="497">one race the human race and</text>
  <text class="quote-line" x="658" y="593">we all belong to it</text>

  <text class="attribution" x="697" y="707">Morris</text>
  <text class="attribution" x="697" y="747">WWII Combat vet ex POW</text>
  <text class="attribution" x="697" y="787">1964.</text>
</svg>
</body>
</html>
```